A5 Flyer for Window Cleaning Company

2 sided Flyer design required for window cleaning company. One side to include we use traditional and hot water fed pole window cleaning systems, conservatory cleaning, and fascia and soffit cleaning. The other side to be for Gutter cleaning. See the must haves section of project brief for more info. Mixture of some images and text for both sides. ( do not have to use all images supplied). The flyer will be used to promote the business to new residential customers.

Target Market(s)

Private households/new customers

Industry/Entity Type

Window Cleaning

Font styles to use
Serif

Requirements
Must have
• Company address ( 7 Old Fenwick Court Marlow Lane Edinburgh EH14 8PJ
Phone numbers( 0131 642 7781 0800 218 5067).
Website and email address ( info@coral-window-cleaning.example)
Excellent Customer Service. Competitive prices. Established 1994.
Side 1of flyer = Coral Window Cleaning Side 2 of flyer Coral Gutter Cleaning.
Nice to have
• Professional look.

```html
<!DOCTYPE html>
<html lang="en">
<head>
<meta charset="utf-8">
<title>Coral Window Cleaning – A5 Flyer</title>
<link rel="stylesheet" href="https://fonts.googleapis.com/css2?family=Playfair+Display:wght@900&family=PT+Serif:wght@400;700&display=swap">
<style>
  :root {
    --navy: #1d5fa2;
    --deep-blue: #1a5ea4;
    --sky: #3fb8fb;
    --bright: #06a3ee;
    --hero-blue: #41aef7;
    --hero-violet: #7a7af0;
    --ink: #111111;
    --white: #ffffff;
    --logo-navy: #2a2f7e;
  }
  * { margin: 0; padding: 0; box-sizing: border-box; }
  html, body { width: 1200px; height: 844px; overflow: hidden; background: var(--white); }
  body { position: relative; font-family: "PT Serif", Georgia, serif; }

  .side-label {
    position: absolute; top: 14px; width: 300px; text-align: center;
    font-size: 19px; color: var(--ink);
  }
  .side-label--front { left: 159px; }
  .side-label--back { left: 742px; }

  .flyer { position: absolute; top: 42px; height: 762px; overflow: hidden; }
  .flyer--front { left: 40px; width: 537px; }
  .flyer--back { left: 622px; width: 540px; border: 1px solid var(--ink); }

  .top-band { position: absolute; left: 0; top: 0; width: 100%; height: 21px; background: var(--deep-blue); }

  .photo { position: absolute; }
  .hero--front {
    left: 0; top: 21px; width: 537px; height: 355px;
    background: linear-gradient(90deg, var(--hero-blue) 0%, #5aa7ec 38%, #b9d4ea 55%, #8da0b4 75%, #5b6f86 100%);
  }
  .hero--front::after {
    content: ""; position: absolute; inset: 0;
    background: linear-gradient(180deg, rgba(65,174,247,0) 50%, rgba(122,122,240,.55) 100%);
  }
  .photo--pole { left: 0; top: 383px; width: 265px; height: 157px; background: linear-gradient(135deg, #e9eef1, #b7c0c6 60%, #4a4e52); }
  .photo--worker { left: 272px; top: 383px; width: 265px; height: 157px; background: linear-gradient(135deg, #6d7d8c, #b9c7d3 50%, #9a3048 80%, #5c6670); }

  .logo {
    position: absolute; display: flex; flex-direction: column; align-items: center; justify-content: center; gap: 6px;
    background: var(--white); color: var(--logo-navy); text-align: center;
    font-weight: 700; line-height: 1.1;
  }
  .logo__mark { width: 14px; height: 14px; background: var(--logo-navy); }
  .logo--front { left: 28px; top: 41px; width: 63px; height: 83px; font-size: 10px; border: 3px solid var(--white); box-shadow: inset 0 0 0 1px #cfd8e6; }
  .logo--back { left: 32px; top: 34px; width: 62px; height: 76px; font-size: 9.5px; }

  .headline {
    position: absolute; font-family: "Playfair Display", Georgia, serif; font-weight: 900;
    text-transform: uppercase; letter-spacing: -0.5px; transform: scaleX(0.86); transform-origin: left top;
  }
  .headline--front { left: 30px; top: 190px; font-size: 56px; line-height: 54px; color: var(--white); }
  .headline--back { left: 30px; top: 136px; font-size: 60px; line-height: 54px; color: var(--ink); }

  .info { position: absolute; left: 0; width: 100%; color: var(--white); }
  .info--front { top: 549px; height: 116px; background: var(--sky); padding: 24px 28px 0; }
  .info__title { font-size: 16px; font-weight: 700; letter-spacing: .2px; line-height: 17px; }
  .info__text { font-size: 12.6px; line-height: 15.4px; letter-spacing: .55px; text-align: justify; }
  .info__promise { font-size: 12.6px; line-height: 15.4px; font-weight: 700; letter-spacing: .4px; margin-top: 6px; }

  .hero--back {
    left: 0; top: 0; width: 540px; height: 318px;
    background: linear-gradient(100deg, #ffffff 0%, #ffffff 30%, #d9dde0 55%, #9c8a6e 75%, #6e6f72 100%);
  }
  .rule { position: absolute; left: 0; width: 100%; background: var(--deep-blue); }
  .rule--upper { top: 318px; height: 7px; }
  .rule--lower { top: 481px; height: 7px; }
  .photo--brush { left: 0; top: 325px; width: 84px; height: 156px; background: linear-gradient(160deg, #9ab8d3, #c9d6e0 60%, #b05040); }
  .photo--house { left: 87px; top: 325px; width: 70px; height: 156px; background: linear-gradient(180deg, #9a4c36, #b8653f 60%, #e8e2d6); }
  .photo--frame { left: 160px; top: 325px; width: 106px; height: 156px; background: linear-gradient(135deg, #3a3a3a, #dfe5e8 45%, #f2f4f5); }
  .photo--conservatory { left: 272px; top: 325px; width: 268px; height: 156px; background: linear-gradient(135deg, #f1f3f4, #b9c3c8 55%, #d73a4a 70%, #2d2f33); }
  .divider { position: absolute; left: 266px; top: 325px; width: 6px; height: 156px; background: var(--deep-blue); }

  .info--back { top: 488px; height: 177px; background: var(--bright); padding: 17px 24px 0 29px; font-size: 13.2px; line-height: 15.4px; letter-spacing: .45px; }
  .services { list-style: none; }
  .services li::before { content: "• "; }

  .contact {
    position: absolute; left: 0; top: 665px; width: 100%; height: 97px; background: var(--navy); color: var(--white);
    padding: 10px 0 0 30px;
  }
  .contact__row { display: flex; align-items: center; white-space: nowrap; }
  .contact__address { font-size: 12.4px; letter-spacing: 1.3px; height: 18px; }
  .contact__phones { font-size: 29px; letter-spacing: 1.6px; height: 36px; margin-top: 4px; }
  .contact__web { font-size: 12.4px; height: 16px; }
  .icon { width: 14px; height: 14px; flex: none; margin-right: 10px; }
  .icon--phone { width: 12px; height: 22px; margin-right: 10px; }
  .sep { margin: 0 18px; }
  .spacer { width: 26px; }
</style>
</head>
<body>

  <div class="side-label side-label--front">A5 Flyer_Front</div>
  <div class="side-label side-label--back">A5 Flyer_Back</div>

  <section class="flyer flyer--front">
    <div class="top-band"></div>
    <div class="photo hero--front" role="img" aria-label="Window cleaner in a blue cap using a washer pad on a large window"></div>
    <div class="logo logo--front"><span class="logo__mark"></span>Coral Window Cleaning</div>
    <h1 class="headline headline--front">Exterior<br>Window<br>Cleaning</h1>
    <div class="photo photo--pole" role="img" aria-label="Water fed pole brush cleaning a white window frame"></div>
    <div class="photo photo--worker" role="img" aria-label="Window cleaner with a squeegee working on an office building"></div>

    <div class="info info--front">
      <h2 class="info__title">NEW WATER FED POLE SYSTEM !</h2>
      <p class="info__text">You may have noticed your rames and sills being cleaned by our staff recently. We've done this free of charge as part of our preparation to get your windows ready for our new Water Fed Pole system.</p>
      <p class="info__promise">Excellent Customer Service • Competitive Prices • Established 1994</p>
    </div>

    <footer class="contact">
      <div class="contact__row contact__address">
        <svg class="icon" viewBox="0 0 14 14"><path d="M7 0a5 5 0 0 0-5 5c0 3.6 5 9 5 9s5-5.4 5-9a5 5 0 0 0-5-5zm0 7a2 2 0 1 1 0-4 2 2 0 0 1 0 4z" fill="#fff"/></svg>
        7 Old Fenwick Court, Marlow Lane, Edinburgh EH14 8PJ
      </div>
      <div class="contact__row contact__phones">
        <svg class="icon icon--phone" viewBox="0 0 12 22"><path d="M5 2h3v5H6c0 3 0 5 0 8h2v5H5C2 20 1 15 1 11S2 2 5 2z" fill="#fff"/></svg>
        0131 642 7781<span class="sep">|</span>0800 218 5067
      </div>
      <div class="contact__row contact__web">
        <svg class="icon" viewBox="0 0 14 14"><rect x="0.5" y="2.5" width="13" height="9" fill="none" stroke="#fff"/><path d="M0.5 2.5 7 8l6.5-5.5" fill="none" stroke="#fff"/></svg>
        info@coral-window-cleaning.example
        <span class="spacer"></span>
        <svg class="icon" viewBox="0 0 14 14"><circle cx="7" cy="7" r="6" fill="none" stroke="#fff"/><path d="M1 7h12M7 1c-3 3-3 9 0 12M7 1c3 3 3 9 0 12" fill="none" stroke="#fff"/></svg>
        www.coral-window-cleaning.example
      </div>
    </footer>
  </section>

  <section class="flyer flyer--back">
    <div class="photo hero--back" role="img" aria-label="Gloved hand pulling autumn leaves out of a roof gutter"></div>
    <div class="logo logo--back"><span class="logo__mark"></span>Coral Gutter Cleaning</div>
    <h1 class="headline headline--back">Gutter<br>and Rhone<br>Cleaning</h1>
    <div class="rule rule--upper"></div>
    <div class="photo photo--brush" role="img" aria-label="Water fed pole brush spraying water against the sky"></div>
    <div class="photo photo--house" role="img" aria-label="Red brick house with white windows"></div>
    <div class="photo photo--frame" role="img" aria-label="Pole brush cleaning a white uPVC window"></div>
    <div class="divider"></div>
    <div class="photo photo--conservatory" role="img" aria-label="Red pole brush cleaning a conservatory roof edge"></div>
    <div class="rule rule--lower"></div>

    <div class="info info--back">
      <p>With our new Water Fed Pole system we can offer you even more services and benefits to those listed below:-</p>
      <ul class="services">
        <li>Exterior window cleaning&nbsp; Gutter cleaning</li>
        <li>Gutter and rhone cleaning</li>
        <li>Fascia and Soffit cleaning</li>
        <li>Conservatory cleaning</li>
        <li>One-off Cleans</li>
        <li>Builders Cleans</li>
      </ul>
      <p class="info__promise">Excellent Customer Service • Competitive Prices • Established 1994</p>
    </div>

    <footer class="contact">
      <div class="contact__row contact__address">
        <svg class="icon" viewBox="0 0 14 14"><path d="M7 0a5 5 0 0 0-5 5c0 3.6 5 9 5 9s5-5.4 5-9a5 5 0 0 0-5-5zm0 7a2 2 0 1 1 0-4 2 2 0 0 1 0 4z" fill="#fff"/></svg>
        7 Old Fenwick Court, Marlow Lane, Edinburgh EH14 8PJ
      </div>
      <div class="contact__row contact__phones">
        <svg class="icon icon--phone" viewBox="0 0 12 22"><path d="M5 2h3v5H6c0 3 0 5 0 8h2v5H5C2 20 1 15 1 11S2 2 5 2z" fill="#fff"/></svg>
        0131 642 7781<span class="sep">|</span>0800 218 5067
      </div>
      <div class="contact__row contact__web">
        <svg class="icon" viewBox="0 0 14 14"><rect x="0.5" y="2.5" width="13" height="9" fill="none" stroke="#fff"/><path d="M0.5 2.5 7 8l6.5-5.5" fill="none" stroke="#fff"/></svg>
        info@coral-window-cleaning.example
        <span class="spacer"></span>
        <svg class="icon" viewBox="0 0 14 14"><circle cx="7" cy="7" r="6" fill="none" stroke="#fff"/><path d="M1 7h12M7 1c-3 3-3 9 0 12M7 1c3 3 3 9 0 12" fill="none" stroke="#fff"/></svg>
        www.coral-window-cleaning.example
      </div>
    </footer>
  </section>

</body>
</html>
```